Business Card Design Project

We need a Business Card for an Mechanical Engineering firm in Singapore. The design should be Modern & Technical looking, yet eye catching.

Our company deals in Cutting Tools & Machine Accessories for the Manufacturing Industries such as Oil & Gas, Aero Space, etc... For more information on our Company, you can either email me or view our website www.torvale.com.sg.

We are trying to revamp our image to give our consumers a fresh new perspective to our company, so we welcome all ideas.

Industry/Entity Type

Business

Requirements
Must have
• Must incorporate New Company Logo into the card as shown in Uploaded file.

```html
<!DOCTYPE html>
<html lang="en">
<head>
<meta charset="utf-8">
<title>Torvale Tools – Business Card</title>
<link href="https://fonts.googleapis.com/css2?family=Saira+Condensed:wght@400&family=Arimo:wght@400;700&display=swap" rel="stylesheet">
<style>
  :root {
    --page-bg: #ecebea;
    --card-bg: #ffffff;
    --brand: #8e1b37;
    --brand-light: #a82444;
    --ink: #4a4a4a;
    --ink-soft: #6a6a6a;
    --divider: #e3a9b6;
  }
  * { margin: 0; padding: 0; box-sizing: border-box; }
  html, body {
    width: 1157px;
    height: 1200px;
    overflow: hidden;
    background: var(--page-bg);
  }
  .canvas {
    position: relative;
    width: 1157px;
    height: 1200px;
  }
  .card {
    position: absolute;
    left: 233px;
    width: 690px;
    height: 415px;
    background: var(--card-bg);
    box-shadow: 0 2px 8px rgba(0,0,0,0.18);
    overflow: hidden;
  }
  .card--front { top: 121px; }
  .card--back { top: 609px; }

  .wordmark {
    position: absolute;
    display: flex;
    align-items: center;
    gap: 14px;
    font-family: "Saira Condensed", "Arial Narrow", sans-serif;
    font-weight: 400;
    color: var(--brand);
    letter-spacing: 1px;
    white-space: nowrap;
    line-height: 1;
  }
  .wordmark__dot {
    border-radius: 50%;
    background: var(--brand);
    flex: none;
  }
  .card--front .wordmark {
    right: 82px;
    top: 278px;
    font-size: 60px;
  }
  .card--front .wordmark__dot { width: 46px; height: 46px; }

  .front-band {
    position: absolute;
    left: 0;
    top: 345px;
    width: 648px;
    height: 22px;
    background: linear-gradient(90deg, var(--brand) 0%, var(--brand-light) 100%);
  }

  .card--back .wordmark {
    left: 38px;
    top: 190px;
    font-size: 36px;
    gap: 9px;
  }
  .card--back .wordmark__dot { width: 26px; height: 26px; }

  .back-divider {
    position: absolute;
    left: 309px;
    top: 46px;
    width: 1px;
    height: 323px;
    background: var(--divider);
  }
  .contact {
    position: absolute;
    left: 358px;
    top: 78px;
    font-family: "Arimo", Arial, sans-serif;
    font-size: 17px;
    color: var(--ink-soft);
    line-height: 1.35;
  }
  .contact__name { font-weight: 700; color: var(--ink); font-size: 17px; }
  .contact__role { color: var(--brand); }
  .contact__address { margin-top: 44px; }
  .contact__list { list-style: none; margin-top: 44px; }
  .contact__list li { display: flex; align-items: center; gap: 9px; }
  .contact__list svg { width: 14px; height: 14px; fill: var(--brand); flex: none; }
</style>
</head>
<body>
<main class="canvas">
  <section class="card card--front" aria-label="Card front">
    <div class="wordmark">
      <span class="wordmark__dot"></span>
      <span class="wordmark__name">TORVALE TOOLS</span>
    </div>
    <div class="front-band"></div>
  </section>

  <section class="card card--back" aria-label="Card back">
    <div class="wordmark">
      <span class="wordmark__dot"></span>
      <span class="wordmark__name">TORVALE TOOLS</span>
    </div>
    <div class="back-divider"></div>
    <div class="contact">
      <p class="contact__name">Name Surname</p>
      <p class="contact__role">Position</p>
      <p class="contact__address">27 Kallang Way #03-12<br>Meridian Industrial Park<br>Singapore, 349870</p>
      <ul class="contact__list">
        <li>
          <svg viewBox="0 0 16 16" aria-hidden="true"><rect x="1" y="1" width="4" height="14" rx="1"/><rect x="6" y="3" width="9" height="12" rx="1"/><rect x="8" y="5" width="5" height="3" fill="#fff"/></svg>
          <span>111-222-333</span>
        </li>
        <li>
          <svg viewBox="0 0 16 16" aria-hidden="true"><circle cx="8" cy="8" r="7"/><path d="M1 8h14M8 1v14M8 1c-3 3-3 11 0 14M8 1c3 3 3 11 0 14" stroke="#fff" stroke-width="1" fill="none"/></svg>
          <span>www.torvale.com.sg</span>
        </li>
        <li>
          <svg viewBox="0 0 16 16" aria-hidden="true"><rect x="1" y="3" width="14" height="10" rx="1"/><path d="M1.5 3.5L8 9l6.5-5.5" stroke="#fff" stroke-width="1.2" fill="none"/></svg>
          <span>email@email.com</span>
        </li>
      </ul>
    </div>
  </section>
</main>
</body>
</html>
```